Quillfern Litigation Funding Letterhead & Document Template

We need a letter head designed for our fund. Our fund works with law firms and investors across the globe. We need a a cover letter template as well as a document template for subsequent pages. Blue and white color scheme is preferred. This is our predecessor's website: https://www.quillfernlc.com/index.html. Please see our logo attached. The logo color code is #19478d. Font is Gotham-Medium.
Target Market(s)
Sophisticated investors and law firms
Font styles to use
Sans Serif
Colors
0255a3

```html
<!DOCTYPE html>
<html lang="en">
<head>
<meta charset="utf-8">
<title>Quillfern Litigation Funding – Letterhead</title>
<link href="https://fonts.googleapis.com/css2?family=Montserrat:wght@500;600&family=Open+Sans:wght@400&display=swap" rel="stylesheet">
<style>
  :root {
    --brand: #19478d;
    --brand-bright: #0255a3;
    --accent-start: #0c3d8f;
    --accent-end: #0a9be0;
    --paper: #e9e9ec;
    --ground: #dfe7e8;
    --ink: #1e2430;
    --watermark: #a9b9d0;
  }
  html, body {
    margin: 0;
    width: 1200px;
    height: 1200px;
    overflow: hidden;
    background: var(--ground);
  }
  .letterhead {
    position: absolute;
    left: 202px;
    top: 30px;
    width: 796px;
    height: 1140px;
    background: var(--paper);
    font-family: "Open Sans", sans-serif;
  }
  .top-band {
    position: absolute;
    left: 249px;
    top: 7px;
    width: 312px;
    height: 17px;
    background: linear-gradient(90deg, var(--accent-start), var(--accent-end));
  }
  .brand {
    position: absolute;
    left: 0;
    right: 0;
    top: 62px;
    text-align: center;
    color: var(--brand);
    font-family: "Montserrat", sans-serif;
    font-weight: 600;
  }
  .brand-mark {
    width: 64px;
    height: 64px;
    margin: 0 auto 22px;
    background: var(--brand);
  }
  .brand-name {
    font-size: 23px;
    letter-spacing: 0.5px;
    line-height: 1;
  }
  .brand-sub {
    display: flex;
    align-items: center;
    justify-content: center;
    gap: 6px;
    margin-top: 4px;
    font-size: 12px;
    letter-spacing: 4px;
    line-height: 1;
  }
  .brand-sub::before, .brand-sub::after {
    content: "";
    width: 96px;
    height: 1.5px;
    background: var(--brand);
  }
  .date-field {
    position: absolute;
    left: 52px;
    top: 228px;
    font-size: 21px;
    color: var(--brand);
    display: flex;
    align-items: flex-end;
  }
  .date-line {
    display: inline-block;
    width: 146px;
    border-bottom: 1.5px solid var(--brand);
    margin-left: 2px;
    margin-bottom: 5px;
  }
  .watermark {
    position: absolute;
    left: 0;
    right: 0;
    top: 545px;
    text-align: center;
    font-family: "Montserrat", sans-serif;
    font-weight: 600;
    font-size: 64px;
    letter-spacing: 2px;
    color: var(--watermark);
    opacity: 0.7;
  }
  .footer {
    position: absolute;
    left: 106px;
    width: 600px;
    top: 1057px;
    border-top: 1.5px solid var(--brand);
    border-bottom: 1.5px solid var(--brand);
    padding: 6px 0 7px;
    text-align: center;
    color: var(--ink);
  }
  .footer-address {
    font-size: 22px;
    line-height: 1.2;
    white-space: nowrap;
  }
  .footer-contacts {
    margin-top: 5px;
    font-size: 11.5px;
    line-height: 1.3;
    letter-spacing: -0.1px;
    display: flex;
    flex-wrap: nowrap;
    justify-content: center;
    gap: 11px;
    white-space: nowrap;
  }
  .footer-contacts .item { flex: 0 0 auto; }
  .footer-contacts .label { color: var(--brand-bright); }
</style>
</head>
<body>
  <main class="letterhead">
    <div class="top-band"></div>

    <header class="brand">
      <div class="brand-mark"></div>
      <div class="brand-name">QUILLFERN LITIGATION</div>
      <div class="brand-sub">FUNDING</div>
    </header>

    <div class="date-field">Date:<span class="date-line"></span></div>

    <div class="watermark">QUILLFERN</div>

    <footer class="footer">
      <div class="footer-address">618 Marlow Avenue Suite 205 Seacliff Bay, CA 90000</div>
      <div class="footer-contacts">
        <span class="item"><span class="label">M:</span> 555-014-2281</span>
        <span class="item"><span class="label">P:</span> 555-017-3306</span>
        <span class="item"><span class="label">E:</span> dana@danamorrow.com</span>
        <span class="item"><span class="label">W:</span> www.danamorrow.com/profile</span>
      </div>
    </footer>
  </main>
</body>
</html>
```